roofing door hanger

we would like to have our logo kvt roofing, it would be given when we are working in the neighborhood and have our services roof replacement, roof repair, ventilation, inspections. Our slogan is "Reliability starts at the top" . Our company is kvt roofing i would like to get one or two reviews from vorblin, and f any pictures are needed can use pellomart.

Industry/Entity Type

Roofing

Requirements
Must have
• this has to be a door hanger design

```html
<!DOCTYPE html>
<html lang="en">
<head>
<meta charset="utf-8">
<title>KVT Roofing Door Hanger</title>
<link rel="stylesheet" href="https://fonts.googleapis.com/css2?family=Open+Sans:wght@700;800&family=Oswald:wght@600;700&display=swap">
<style>
  :root {
    --stage: #e4e4e2;
    --charcoal: #2e3238;
    --charcoal-deep: #1f2124;
    --orange: #f2841c;
    --ink: #1c1c1c;
    --white: #ffffff;
    --badge-red: #d9262b;
  }
  * { margin: 0; padding: 0; box-sizing: border-box; }
  html, body { width: 1200px; height: 1200px; overflow: hidden; background: var(--stage); }
  .door-hanger {
    position: absolute; left: 390px; top: 90px;
    width: 420px; height: 1020px;
    background: var(--charcoal);
    overflow: hidden;
    font-family: "Open Sans", sans-serif;
    box-shadow: 0 6px 18px rgba(0,0,0,0.18);
  }
  .hanger-hole {
    position: absolute; left: 142px; top: 94px; width: 132px; height: 132px;
    border-radius: 50%; background: var(--stage);
  }
  .hero-photo {
    position: absolute; left: 0; top: 190px; width: 420px; height: 300px;
    background: linear-gradient(160deg, #3a3d42 0%, #34373b 45%, #2b2d31 100%);
  }
  .brand-name {
    position: absolute; left: 0; right: 0; top: 318px; text-align: center;
    font-weight: 800; font-size: 42px; letter-spacing: 2px; color: var(--orange);
  }
  .slogan {
    position: absolute; left: 0; right: 0; top: 408px; text-align: center;
    font-weight: 700; font-size: 21px; color: var(--white);
  }
  .panel { position: absolute; left: 0; top: 0; }
  .services-title {
    position: absolute; left: 27px; top: 518px;
    font-family: "Oswald", sans-serif; font-weight: 700; font-size: 42px;
    color: var(--ink); letter-spacing: -0.5px;
  }
  .service-list { position: absolute; left: 27px; top: 584px; list-style: none; }
  .service-list li {
    display: flex; align-items: center; height: 45px;
    font-weight: 700; font-size: 24px; color: var(--white); letter-spacing: 0.3px;
  }
  .service-list svg { width: 26px; height: 26px; margin-right: 14px; }
  .photo-circle {
    position: absolute; border-radius: 50%; border: 6px solid var(--charcoal-deep);
  }
  .photo-crew { left: 258px; top: 622px; width: 136px; height: 136px;
    background: linear-gradient(170deg, #6e9fd0 0%, #8fa7bd 40%, #55585d 75%); }
  .photo-shingles { left: 239px; top: 769px; width: 110px; height: 110px;
    background: linear-gradient(150deg, #9a9da1 0%, #6f7277 60%, #4c4e52 100%); }
  .photo-hands { left: 224px; top: 888px; width: 92px; height: 92px;
    background: linear-gradient(140deg, #2e4f8a 0%, #7a7e86 55%, #c9c9c9 100%); }
  .call-label {
    position: absolute; left: 32px; top: 800px;
    font-weight: 800; font-size: 19px; color: var(--white); letter-spacing: 0.5px;
  }
  .phone {
    position: absolute; left: 31px; top: 832px;
    font-family: "Oswald", sans-serif; font-weight: 700; font-size: 38px;
    color: var(--ink); letter-spacing: -0.5px;
  }
  .website {
    position: absolute; left: 31px; top: 885px;
    font-weight: 800; font-size: 15px; color: var(--ink);
  }
  .partner-badge {
    position: absolute; left: 29px; top: 934px; width: 151px; height: 44px;
    background: var(--white); display: flex; align-items: center; padding-left: 4px;
  }
  .partner-badge span { display: block; width: 40px; height: 36px; background: var(--badge-red); }
</style>
</head>
<body>
  <main class="door-hanger">
    <div class="hero-photo" role="img" aria-label="Dusk photo of roofers working on a shingled roof"></div>
    <div class="hanger-hole"></div>

    <div class="brand-name">KVT ROOFING</div>
    <p class="slogan">RELIABILITY STARTS AT THE TOP</p>

    <svg class="panel" width="420" height="1020" viewBox="0 0 420 1020" aria-hidden="true">
      <rect x="0" y="440" width="420" height="580" fill="#1f2124"/>
      <path d="M-10,460 C5,446 25,442 45,448 L378,534 C408,543 420,565 412,595 L280,1030 L-10,1030 Z"
            fill="#f2841c" stroke="#ffffff" stroke-width="9" stroke-linejoin="round"/>
    </svg>

    <h2 class="services-title">OUR SERVICES</h2>
    <ul class="service-list">
      <li><svg viewBox="0 0 26 26"><path d="M3 14 L10 21 L23 5" fill="none" stroke="#fff" stroke-width="5" stroke-linecap="round" stroke-linejoin="round"/></svg>ROOF REPLACEMENT</li>
      <li><svg viewBox="0 0 26 26"><path d="M3 14 L10 21 L23 5" fill="none" stroke="#fff" stroke-width="5" stroke-linecap="round" stroke-linejoin="round"/></svg>ROOF REPAIR</li>
      <li><svg viewBox="0 0 26 26"><path d="M3 14 L10 21 L23 5" fill="none" stroke="#fff" stroke-width="5" stroke-linecap="round" stroke-linejoin="round"/></svg>VENTILATION</li>
      <li><svg viewBox="0 0 26 26"><path d="M3 14 L10 21 L23 5" fill="none" stroke="#fff" stroke-width="5" stroke-linecap="round" stroke-linejoin="round"/></svg>INSPECTIONS</li>
    </ul>

    <div class="photo-circle photo-crew" role="img" aria-label="Roofers installing shingles under blue sky"></div>
    <div class="photo-circle photo-shingles" role="img" aria-label="Close-up of damaged grey shingles"></div>
    <div class="photo-circle photo-hands" role="img" aria-label="Gloved hands fixing a shingle"></div>

    <p class="call-label">CALL US TODAY</p>
    <p class="phone">555-014-2286</p>
    <p class="website">www.kvt-roofing.com</p>

    <div class="partner-badge" role="img" aria-label="Preferred contractor badge"><span></span></div>
  </main>
</body>
</html>
```